RJ Penhall & Associates

Create a website encompassing design work already carried out for business card.
Small accounting practice, business accounting and management, superannuation, audit, taxation.

```html
<!DOCTYPE html>
<html lang="en">
<head>
<meta charset="utf-8">
<title>RJ Penhall &amp; Associates</title>
<link rel="stylesheet" href="https://fonts.googleapis.com/css2?family=Arimo:wght@400;700&family=Tinos&display=swap">
<style>
:root{
  --blue:#0a84cf;
  --blue-soft:#3fa4e0;
  --grey-band:#ececec;
  --grey-shape:#c9c9c9;
  --grey-line:#b5b5b5;
  --ink:#333;
  --ink-soft:#666;
  --white:#fff;
}
*{box-sizing:border-box;margin:0;padding:0}
html,body{width:1200px;height:900px;overflow:hidden;background:var(--white)}
body{font-family:"Arimo",Arial,sans-serif;color:var(--ink);position:relative}
.site{position:absolute;left:495px;top:0;width:222px;height:882px}
.abs{position:absolute}
.center{left:0;width:222px;text-align:center}

/* hero */
.hero{top:0;left:0;width:222px;height:130px;background:var(--blue);color:var(--white)}
.brand{position:absolute;top:22px;left:0;width:222px;display:flex;justify-content:center;align-items:center;gap:5px}
.brand-mark{width:12px;height:12px;background:var(--white);border-radius:50%}
.brand-name{font-family:"Arimo",Arial,sans-serif;font-weight:700;font-size:9px;line-height:12px;color:var(--white);white-space:nowrap}
.hero-title{top:72px;font-weight:700;font-size:8.5px}
.hero-sub{top:85px;left:16px;width:190px;text-align:center;font-size:4.4px;line-height:5.6px;font-weight:700}
.hero-down{top:103px;left:99px}

/* nav */
.nav{top:130px;left:0;width:222px;height:19px;background:var(--white);display:flex;align-items:center;padding:0 17px 0 20px;justify-content:space-between}
.nav-brand{display:flex;align-items:center;gap:3px;font-family:"Arimo",Arial,sans-serif;font-size:4.6px;color:var(--ink-soft);white-space:nowrap}
.nav-brand i{width:7px;height:7px;border-radius:50%;background:var(--blue-soft);display:block}
.nav-links{display:flex;gap:5px;font-size:3.4px;list-style:none;color:var(--ink)}
.nav-links .active{color:var(--blue)}

/* sections */
.band{left:0;width:222px;background:var(--grey-band)}
.section-title{font-size:8.5px;color:var(--ink)}
.section-title span{color:var(--blue)}
.section-title b{font-weight:400;position:relative;display:inline-block;padding:0 3px}
.section-title b::before,.section-title b::after{content:"";position:absolute;width:6px;height:6px;border-color:var(--grey-line);border-style:solid}
.section-title b::after{right:-6px;top:-6px;border-width:1px 1px 0 0}
.section-title b::before{left:-6px;bottom:-6px;border-width:0 0 1px 1px}

.services{top:149px;height:148px}
.service{position:absolute;top:52px;width:40px;text-align:center}
.service svg{display:block;margin:0 auto}
.service h3{font-size:4.6px;font-weight:400;margin-top:2px;color:var(--ink)}
.service p{font-size:3px;line-height:4.4px;color:var(--ink-soft);margin-top:3px;padding:0 3px}

.about-text{top:345px;left:42px;width:138px;font-size:4.2px;line-height:5.1px;text-align:center;color:#555}
.about-art{top:416px;left:73px;width:68px;height:68px;border-radius:50%;background:radial-gradient(circle at 50% 45%,#2a9ae0,var(--blue))}

.team{top:508px;height:183px}
.member{position:absolute;top:90px;width:50px;text-align:center}
.member-photo{width:40px;height:40px;margin:0 auto;border-radius:50%;background:var(--grey-shape);font-size:4px;color:#888;display:flex;align-items:center;justify-content:center}
.member h3{font-size:4.4px;font-weight:400;margin-top:14px}
.member p{font-size:3.2px;color:var(--ink-soft);margin-top:3px}
.member-social{display:flex;justify-content:center;gap:4px;margin-top:4px}
.member-social i{width:8px;height:8px;border:0.6px solid #777;border-radius:50%;display:block}

/* contact */
.field{left:22px;width:85px;border:1px solid #555;background:var(--white);font-size:3.6px;color:#999;padding:3px 4px}
.send{top:845px;left:22px;width:37px;height:11px;background:var(--blue);color:var(--white);font-size:3.6px;font-weight:700;display:flex;align-items:center;justify-content:center;border:0}
.contact-copy{top:757px;left:118px;width:84px;font-size:3.9px;line-height:4.8px}
.contact-address{top:786px;left:118px;width:96px;font-family:"Tinos",serif;font-size:5.2px;line-height:6.2px;font-style:normal}
.contact-gap{display:block;height:5px}
.contact-social{top:826px;left:118px;display:flex;gap:5px}
.contact-social i{width:13px;height:13px;border:0.7px solid #555;border-radius:50%;display:block}
.footer{top:874px;font-size:4px;color:var(--ink-soft)}
</style>
</head>
<body>
<main class="site">
  <header class="abs hero">
    <div class="brand"><span class="brand-mark"></span><span class="brand-name">RJ Penhall &amp; Associates</span></div>
    <h1 class="abs center hero-title">Fusce rutrum pretium lorem semper nulla.</h1>
    <p class="abs hero-sub">Vestibulum ornare cursus nisl, fermentum tincidunt libero pretium at. Maecenas interdum ligula non fermentum fringilla.</p>
    <svg class="abs hero-down" width="17" height="17" viewBox="0 0 17 17"><circle cx="8.5" cy="8.5" r="7.8" fill="none" stroke="#fff" stroke-width="0.9"/><path d="M5.2 7.2 8.5 10.3 11.8 7.2" fill="none" stroke="#fff" stroke-width="0.9"/></svg>
  </header>

  <nav class="abs nav">
    <div class="nav-brand"><i></i><span>RJ Penhall &amp; Associates</span></div>
    <ul class="nav-links"><li>HOME</li><li class="active">SERVICES</li><li>ABOUT</li><li>TEAM</li><li>CONTACT</li></ul>
  </nav>

  <section class="abs band services">
    <h2 class="abs center section-title" style="top:16px"><b>Our <span>Services</span></b></h2>
    <div class="service" style="left:6px">
      <svg width="32" height="32" viewBox="0 0 32 32"><polygon points="16,2 28,9 28,23 16,30 4,23 4,9" fill="#fff" stroke="var(--blue)" stroke-width="2.2" stroke-linejoin="round"/><rect x="12" y="10" width="8" height="12" fill="none" stroke="var(--blue)" stroke-width="1.2"/><path d="M13.5 13h5M13.5 16h5M13.5 19h5" stroke="var(--blue)" stroke-width="0.8"/></svg>
      <h3>Accountant</h3><p>Careful bookkeeping and clear yearly accounts for owners who value their time.</p>
    </div>
    <div class="service" style="left:46px">
      <svg width="32" height="32" viewBox="0 0 32 32"><polygon points="16,2 28,9 28,23 16,30 4,23 4,9" fill="#ddd" stroke="var(--grey-shape)" stroke-width="2.2" stroke-linejoin="round"/><path d="M10 17l4-4 4 3 4-4" fill="none" stroke="#fff" stroke-width="1.6"/></svg>
      <h3>Business Solutions</h3><p>Practical plans for cash flow, pricing and growth tailored to each small business.</p>
    </div>
    <div class="service" style="left:87px">
      <svg width="32" height="32" viewBox="0 0 32 32"><polygon points="16,2 28,9 28,23 16,30 4,23 4,9" fill="#ddd" stroke="var(--grey-shape)" stroke-width="2.2" stroke-linejoin="round"/><path d="M11 11v10M16 11v10M21 11v10M11 16h10" stroke="#fff" stroke-width="1.6"/></svg>
      <h3>Management</h3><p>Monthly reporting and budgeting support so decisions rest on sound numbers.</p>
    </div>
    <div class="service" style="left:127px">
      <svg width="32" height="32" viewBox="0 0 32 32"><polygon points="16,2 28,9 28,23 16,30 4,23 4,9" fill="#ddd" stroke="var(--grey-shape)" stroke-width="2.2" stroke-linejoin="round"/><circle cx="16" cy="17" r="4.5" fill="none" stroke="#fff" stroke-width="1.6"/></svg>
      <h3>Superannuation</h3><p>Fund setup, compliance and annual returns handled with steady, patient care.</p>
    </div>
    <div class="service" style="left:168px">
      <svg width="32" height="32" viewBox="0 0 32 32"><polygon points="16,2 28,9 28,23 16,30 4,23 4,9" fill="#ddd" stroke="var(--grey-shape)" stroke-width="2.2" stroke-linejoin="round"/><rect x="12" y="10" width="8" height="12" fill="none" stroke="#fff" stroke-width="1.4"/></svg>
      <h3>Audit</h3><p>Independent audits for funds and associations, delivered on time and thoroughly.</p>
    </div>
  </section>

  <section>
    <h2 class="abs center section-title" style="top:317px"><b>About <span>us</span></b></h2>
    <p class="abs about-text">Aliquam metus neque, bibendum sit amet porta at, consequat et enim. In ut turpis non ipsum rhoncus porttitor vel ac nunc. Maecenas interdum dignissim lorem quis auctor. Donec sit amet nulla nisl, aliquam pretium ipsum. Pellentesque sodales ipsum et enim rutrum adipiscing. Quisque tincidunt mattis sapien, vel posuere. Aliquam metus neque, bibendum sit amet porta at, consequat et enim. In ut turpis non ipsum rhoncus porttitor vel ac nunc. Maecenas interdum dignissim lorem quis auctor. Donec sit amet nulla nisl, aliquam pretium ipsum. Pellentesque sodales ipsum et enim rutrum adipiscing. Quisque tincidunt mattis sapien, vel posuere.</p>
    <div class="abs about-art" role="img" aria-label="Illustration of an open hand holding a growing seedling with a dollar coin, on a blue circle"></div>
  </section>

  <section class="abs band team">
    <h2 class="abs center section-title" style="top:19px"><b>Our <span>Team</span></b></h2>
    <svg class="abs" style="left:96px;top:53px" width="23" height="12" viewBox="0 0 23 12"><polygon points="6,0.5 11,3.2 11,8.8 6,11.5 1,8.8 1,3.2" fill="var(--blue)"/><polygon points="17,0.5 22,3.2 22,8.8 17,11.5 12,8.8 12,3.2" fill="var(--blue)"/><path d="M7 4 5 6l2 2M16 4l2 2-2 2" fill="none" stroke="#fff" stroke-width="0.8"/></svg>
    <div class="member" style="left:17px"><div class="member-photo">Member Photo</div><h3>Member Name</h3><p>CEO / Marketing Guru</p><div class="member-social"><i></i><i></i></div></div>
    <div class="member" style="left:81px"><div class="member-photo">Member Photo</div><h3>Member Name</h3><p>CEO / Marketing Guru</p><div class="member-social"><i></i><i></i></div></div>
    <div class="member" style="left:145px"><div class="member-photo">Member Photo</div><h3>Member Name</h3><p>CEO / Marketing Guru</p><div class="member-social"><i></i><i></i></div></div>
  </section>

  <section>
    <h2 class="abs center section-title" style="top:717px"><b>Get <span>in touch</span></b></h2>
    <div class="abs field" style="top:758px;height:12px">Your Name</div>
    <div class="abs field" style="top:776px;height:12px">Your Email</div>
    <div class="abs field" style="top:794px;height:45px">Your Message</div>
    <div class="abs send">Send email</div>
    <p class="abs contact-copy">Lorem ipsum dolor sit amet, consectetuer adipiscing elit. Donec odio. Quisque volutpat mattis eros. Nullam malesuada erat ut turpis. Suspendisse urna nibh, viverra non, semper suscipit, posuere a, pede.</p>
    <address class="abs contact-address">Address Line 1, Address Line 2,<br>State with Zip Code, Country.<span class="contact-gap"></span>T. ( COD ) Telephone Number<br>M. ( COD ) Mobile Number</address>
    <div class="abs contact-social"><i></i><i></i><i></i></div>
    <footer class="abs center footer">RJ Penhall &amp; Associates</footer>
  </section>
</main>
</body>
</html>
```